Brookmere Osteopathy flyer

I want a clean clear DL flyer (but also want an A4 poster) promoting a new Osteopathic business in a semi rural area in Tasmania (Australia).
It can have pictures like the examples attached to show people what Osteopathy is (its like Chiropractic and physiotherapy).
I am the sole practioner and am male, so any pictures would be best to be a white male if possible.
I've attached some wording, you can use all, or none of it
I don't have a phone number for the business yet
info@brookmereosteopathy.example
www.brookmereosteopathy.example
Target Market(s)
Australians, from tradies, professionals, babies to retired people
Industry/Entity Type
Health
Look and feel

```html
<!DOCTYPE html>
<html lang="en">
<head>
<meta charset="utf-8">
<title>Brookmere Osteopathy – A4 poster and DL flyer</title>
<link rel="stylesheet" href="https://fonts.googleapis.com/css2?family=Fjalla+One&family=Montserrat:wght@300;400;600;800&family=Roboto+Condensed:wght@300;400;700&display=swap">
<style>
  :root {
    --blue: #1197d4;
    --orange: #f7923a;
    --ink: #1d1d1b;
    --white: #ffffff;
    --backdrop: #e7e4df;
    --photo-light: #e9edf1;
    --photo-mid: #c9ced4;
    --photo-dark: #27344a;
  }
  * { box-sizing: border-box; margin: 0; padding: 0; }
  html, body { width: 1200px; height: 904px; overflow: hidden; }
  body { background: var(--backdrop); position: relative; font-family: "Montserrat", sans-serif; color: var(--ink); }

  .sheet { position: absolute; top: 95px; height: 717px; background: var(--white); overflow: hidden; box-shadow: 0 6px 18px rgba(0,0,0,.18); }
  .sheet--a4 { left: 91px; width: 507px; }
  .sheet--dl { left: 647px; width: 329px; }
  .sheet__art { position: absolute; inset: 0; }

  .headline { position: absolute; font-family: "Fjalla One", sans-serif; text-transform: uppercase; line-height: 1.12; letter-spacing: -.3px; }
  .headline__move { color: var(--orange); display: block; }
  .headline__feel { color: var(--blue); display: block; }
  .sheet--a4 .headline { left: 29px; top: 24px; font-size: 32px; }
  .sheet--dl .headline { right: 20px; top: 17px; font-size: 20px; text-align: right; }

  .brand-seal { position: absolute; border-radius: 50%; background: var(--white); border: 3px solid var(--blue); display: flex; align-items: center; justify-content: center; text-align: center; }
  .brand-seal__name { font-family: "Montserrat", sans-serif; font-weight: 800; color: var(--blue); text-transform: uppercase; line-height: 1.25; }
  .sheet--a4 .brand-seal { left: 290px; top: 152px; width: 156px; height: 156px; }
  .sheet--a4 .brand-seal__name { font-size: 14px; }
  .sheet--dl .brand-seal { left: 36px; top: 107px; width: 100px; height: 100px; border-width: 2px; }
  .sheet--dl .brand-seal__name { font-size: 9px; }

  .reasons-title { position: absolute; font-family: "Montserrat", sans-serif; font-weight: 800; color: var(--ink); }
  .sheet--a4 .reasons-title { left: 30px; top: 310px; font-size: 16.5px; letter-spacing: -.2px; }
  .sheet--dl .reasons-title { left: 20px; top: 205px; font-family: "Roboto Condensed", sans-serif; font-weight: 700; font-size: 18px; line-height: 22px; text-transform: uppercase; }

  .tile { position: absolute; border-radius: 4px; color: var(--white); display: flex; flex-direction: column; align-items: center; justify-content: flex-end; text-align: center; font-family: "Roboto Condensed", sans-serif; font-weight: 700; line-height: 1.2; }
  .tile--orange { background: var(--orange); }
  .tile--blue { background: var(--blue); }
  .tile__icon { background: rgba(255,255,255,.22); border-radius: 6px; }
  .sheet--a4 .tile { width: 85px; height: 75px; padding-bottom: 6px; font-size: 8.6px; gap: 4px; }
  .sheet--a4 .tile__icon { width: 36px; height: 36px; }
  .sheet--dl .tile { width: 92px; height: 80px; padding-bottom: 7px; font-size: 9.4px; gap: 5px; }
  .sheet--dl .tile__icon { width: 36px; height: 38px; }

  .about { position: absolute; font-weight: 300; text-align: justify; }
  .about strong { font-weight: 600; }
  .sheet--a4 .about { left: 31px; top: 498px; width: 445px; font-size: 8.9px; line-height: 12px; letter-spacing: -.1px; }
  .sheet--dl .about { left: 21px; top: 546px; width: 287px; font-family: "Roboto Condensed", sans-serif; font-size: 8.4px; line-height: 11.4px; }
  .sheet--dl .about strong { font-weight: 700; }

  .call { position: absolute; color: var(--white); font-family: "Montserrat", sans-serif; }
  .call__label { font-weight: 800; display: block; white-space: nowrap; }
  .call__phone { font-weight: 400; display: flex; align-items: center; white-space: nowrap; }
  .sheet--a4 .call { left: 29px; top: 646px; }
  .sheet--a4 .call__label { font-size: 22px; }
  .sheet--a4 .call__phone { font-size: 21px; gap: 7px; margin-top: 2px; }
  .sheet--dl .call { left: 21px; top: 671px; }
  .sheet--dl .call__label { font-size: 14.5px; }
  .sheet--dl .call__phone { font-size: 14px; gap: 4px; }

  .contact { position: absolute; list-style: none; color: var(--white); font-weight: 400; }
  .contact li { display: flex; align-items: center; white-space: nowrap; }
  .sheet--a4 .contact { left: 232px; top: 637px; font-size: 12px; }
  .sheet--a4 .contact li { height: 21.5px; gap: 7px; }
  .sheet--dl .contact { left: 149px; top: 666px; font-size: 7.3px; font-weight: 600; }
  .sheet--dl .contact li { height: 14px; gap: 4px; }

  .icon-dot { flex: none; border-radius: 50%; background: var(--orange); display: flex; align-items: center; justify-content: center; }
  .sheet--a4 .contact .icon-dot { width: 17px; height: 17px; }
  .sheet--dl .contact .icon-dot { width: 11px; height: 11px; }
  .sheet--a4 .call .icon-dot { width: 22px; height: 22px; }
  .sheet--dl .call .icon-dot { width: 13px; height: 13px; }
  .icon-dot svg { width: 62%; height: 62%; }
</style>
</head>
<body>

<section class="sheet sheet--a4" aria-label="Brookmere Osteopathy A4 poster">
  <svg class="sheet__art" width="507" height="717" viewBox="0 0 507 717">
    <defs>
      <linearGradient id="a4-photo" x1="0" y1="0" x2="1" y2="1">
        <stop offset="0" stop-color="var(--photo-light)"/>
        <stop offset=".55" stop-color="var(--photo-mid)"/>
        <stop offset="1" stop-color="var(--photo-dark)"/>
      </linearGradient>
    </defs>
    <path role="img" aria-label="Photo: osteopath's hands supporting a relaxed patient's head and neck on a treatment table"
          d="M0 0H507V292C470 268 430 240 380 236C300 230 230 262 150 254C90 248 40 230 0 214Z" fill="url(#a4-photo)"/>
    <path role="img" aria-label="Decorative spine vertebrae band"
          d="M0 222C40 240 90 258 150 262C230 268 300 240 380 244C430 248 470 276 507 300V312C470 290 430 262 380 262C300 262 230 294 150 290C90 286 40 266 0 246Z" fill="var(--blue)"/>
    <path role="img" aria-label="Decorative spine vertebrae band on blue footer"
          d="M0 570C80 592 160 574 250 568C340 562 420 582 507 625V717H0Z" fill="var(--blue)"/>
  </svg>

  <h1 class="headline"><span class="headline__move">Move better,</span><span class="headline__feel">Feel better.</span></h1>

  <div class="brand-seal"><span class="brand-seal__name">Brookmere<br>Osteopathy</span></div>

  <h2 class="reasons-title">Common reasons people visit an osteopath:</h2>

  <div class="tile tile--orange" style="left:31px;top:337px"><span class="tile__icon" role="img" aria-label="Back and neck icon"></span>Back / neck pain</div>
  <div class="tile tile--blue" style="left:121px;top:337px"><span class="tile__icon" role="img" aria-label="Headache icon"></span>Headaches<br>/ migraines</div>
  <div class="tile tile--orange" style="left:211px;top:337px"><span class="tile__icon" role="img" aria-label="Joint and muscle icon"></span>Joint and<br>muscle pain</div>
  <div class="tile tile--blue" style="left:302px;top:337px"><span class="tile__icon" role="img" aria-label="Pregnancy icon"></span>Pregnancy-related<br>discomfort</div>
  <div class="tile tile--orange" style="left:392px;top:337px"><span class="tile__icon" role="img" aria-label="Spinal disc icon"></span>Disc related<br>issues</div>
  <div class="tile tile--blue" style="left:31px;top:417px"><span class="tile__icon" role="img" aria-label="Hip and sciatic nerve icon"></span>Sciatica</div>
  <div class="tile tile--orange" style="left:121px;top:417px"><span class="tile__icon" role="img" aria-label="Foot icon"></span>Plantar fasciitis</div>
  <div class="tile tile--blue" style="left:211px;top:417px"><span class="tile__icon" role="img" aria-label="Knee joint icon"></span>Tendonitis<br>/ Bursitis</div>
  <div class="tile tile--orange" style="left:302px;top:417px"><span class="tile__icon" role="img" aria-label="Shoulder icon"></span>Adhesive capsulitis<br>(frozen shoulder)</div>
  <div class="tile tile--blue" style="left:392px;top:417px"><span class="tile__icon" role="img" aria-label="Elbow icon"></span>Tennis /<br>Golfers elbow</div>

  <p class="about">Brookmere Osteopathy use a tailored combination of <strong>joint mobilisation/manipulation, stretching, movement, trigger point dry needling and targeted massage</strong> to reduce pain and restore optimal function. Hands-on treatment is backed up with rehabilitative exercise prescription and advice. So whether you're recovering from injury or managing chronic discomfort, we're here to help you move better and feel your best.</p>

  <div class="call">
    <span class="call__label">CALL US TODAY</span>
    <span class="call__phone"><span class="icon-dot"><svg viewBox="0 0 24 24"><path d="M6.6 10.8a15 15 0 0 0 6.6 6.6l2.2-2.2c.3-.3.7-.4 1-.2 1.1.4 2.3.6 3.6.6.6 0 1 .4 1 1V20c0 .6-.4 1-1 1A17 17 0 0 1 3 4c0-.6.4-1 1-1h3.5c.6 0 1 .4 1 1 0 1.3.2 2.5.6 3.6.1.3 0 .7-.2 1z" fill="#fff"/></svg></span>(03) 5550 1234</span>
  </div>

  <ul class="contact">
    <li><span class="icon-dot"><svg viewBox="0 0 24 24"><path d="M12 2a7 7 0 0 0-7 7c0 5 7 13 7 13s7-8 7-13a7 7 0 0 0-7-7zm0 9.5a2.5 2.5 0 1 1 0-5 2.5 2.5 0 0 1 0 5z" fill="#fff"/></svg></span>24 Riverbend Road, Brookmere</li>
    <li><span class="icon-dot"><svg viewBox="0 0 24 24"><circle cx="12" cy="12" r="9" fill="none" stroke="#fff" stroke-width="2"/><path d="M3 12h18M12 3c3 3 3 15 0 18M12 3c-3 3-3 15 0 18" fill="none" stroke="#fff" stroke-width="1.6"/></svg></span>www.brookmereosteopathy.example</li>
    <li><span class="icon-dot"><svg viewBox="0 0 24 24"><rect x="3" y="6" width="18" height="12" rx="1.5" fill="#fff"/><path d="M3 7l9 6 9-6" fill="none" stroke="#f7923a" stroke-width="1.6"/></svg></span>info@brookmereosteopathy.example</li>
  </ul>
</section>

<section class="sheet sheet--dl" aria-label="Brookmere Osteopathy DL flyer">
  <svg class="sheet__art" width="329" height="717" viewBox="0 0 329 717">
    <defs>
      <linearGradient id="dl-photo" x1="0" y1="0" x2="1" y2="1">
        <stop offset="0" stop-color="var(--photo-light)"/>
        <stop offset=".55" stop-color="var(--photo-mid)"/>
        <stop offset="1" stop-color="var(--photo-dark)"/>
      </linearGradient>
    </defs>
    <path role="img" aria-label="Photo: osteopath's hands supporting a relaxed patient's head and neck on a treatment table"
          d="M0 0H329V146C290 150 250 150 200 160C140 172 80 185 0 190Z" fill="url(#dl-photo)"/>
    <path role="img" aria-label="Decorative spine vertebrae band"
          d="M0 184C60 180 110 166 160 158C220 150 280 142 329 136V158C280 164 220 172 160 180C110 188 60 196 0 198Z" fill="var(--blue)"/>
    <path role="img" aria-label="Decorative spine vertebrae band on blue footer"
          d="M0 618C60 605 120 600 180 605C240 610 290 635 329 660V717H0Z" fill="var(--blue)"/>
  </svg>

  <h1 class="headline"><span class="headline__move">Move better,</span><span class="headline__feel">Feel better.</span></h1>

  <div class="brand-seal"><span class="brand-seal__name">Brookmere<br>Osteopathy</span></div>

  <h2 class="reasons-title">Common reasons<br>people visit<br>an osteopath:</h2>

  <div class="tile tile--orange" style="left:216px;top:202px"><span class="tile__icon" role="img" aria-label="Back and neck icon"></span>Back / neck pain</div>
  <div class="tile tile--blue" style="left:21px;top:288px"><span class="tile__icon" role="img" aria-label="Headache icon"></span>Headaches<br>/ migraines</div>
  <div class="tile tile--orange" style="left:119px;top:288px"><span class="tile__icon" role="img" aria-label="Joint and muscle icon"></span>Joint and<br>muscle pain</div>
  <div class="tile tile--blue" style="left:216px;top:288px"><span class="tile__icon" role="img" aria-label="Pregnancy icon"></span>Pregnancy-related<br>discomfort</div>
  <div class="tile tile--orange" style="left:21px;top:374px"><span class="tile__icon" role="img" aria-label="Spinal disc icon"></span>Disc related<br>issues</div>
  <div class="tile tile--blue" style="left:119px;top:374px"><span class="tile__icon" role="img" aria-label="Hip and sciatic nerve icon"></span>Sciatica</div>
  <div class="tile tile--orange" style="left:216px;top:374px"><span class="tile__icon" role="img" aria-label="Foot icon"></span>Plantar fasciitis</div>
  <div class="tile tile--blue" style="left:21px;top:460px"><span class="tile__icon" role="img" aria-label="Knee joint icon"></span>Tendonitis<br>/ Bursitis</div>
  <div class="tile tile--orange" style="left:119px;top:460px"><span class="tile__icon" role="img" aria-label="Shoulder icon"></span>Adhesive capsulitis<br>(frozen shoulder)</div>
  <div class="tile tile--blue" style="left:216px;top:460px"><span class="tile__icon" role="img" aria-label="Elbow icon"></span>Tennis /<br>Golfers elbow</div>

  <p class="about">Brookmere Osteopathy use a tailored combination of <strong>joint mobilisation/ manipulation, stretching, movement, trigger point dry needling &amp; targeted massage</strong> to reduce pain &amp; restore optimal function. Hands-on treatment is backed up with rehabilitative exercise prescription &amp; advice. So whether you're recovering from injury or managing chronic discomfort, we're here to help you move better &amp; feel your best.</p>

  <div class="call">
    <span class="call__label">CALL US TODAY</span>
    <span class="call__phone"><span class="icon-dot"><svg viewBox="0 0 24 24"><path d="M6.6 10.8a15 15 0 0 0 6.6 6.6l2.2-2.2c.3-.3.7-.4 1-.2 1.1.4 2.3.6 3.6.6.6 0 1 .4 1 1V20c0 .6-.4 1-1 1A17 17 0 0 1 3 4c0-.6.4-1 1-1h3.5c.6 0 1 .4 1 1 0 1.3.2 2.5.6 3.6.1.3 0 .7-.2 1z" fill="#fff"/></svg></span>(03) 5550 1234</span>
  </div>

  <ul class="contact">
    <li><span class="icon-dot"><svg viewBox="0 0 24 24"><path d="M12 2a7 7 0 0 0-7 7c0 5 7 13 7 13s7-8 7-13a7 7 0 0 0-7-7zm0 9.5a2.5 2.5 0 1 1 0-5 2.5 2.5 0 0 1 0 5z" fill="#fff"/></svg></span>24 Riverbend Road, Brookmere</li>
    <li><span class="icon-dot"><svg viewBox="0 0 24 24"><circle cx="12" cy="12" r="9" fill="none" stroke="#fff" stroke-width="2"/><path d="M3 12h18M12 3c3 3 3 15 0 18M12 3c-3 3-3 15 0 18" fill="none" stroke="#fff" stroke-width="1.6"/></svg></span>www.brookmereosteopathy.example</li>
    <li><span class="icon-dot"><svg viewBox="0 0 24 24"><rect x="3" y="6" width="18" height="12" rx="1.5" fill="#fff"/><path d="M3 7l9 6 9-6" fill="none" stroke="#f7923a" stroke-width="1.6"/></svg></span>info@brookmereosteopathy.example</li>
  </ul>
</section>

</body>
</html>
```